Looking for a web design for event planning. Targeting the Wedding Industry, Corporate Meetings, Special Events, Fundraisers and other Celebratory Events
Home Page - name with pictures of various events- 3 buttons to go to
Wedding ( engagement parties, bridal showers, rehearsal dinners, welcome receptions and wedding receptions page
Corporate Meetings/Fundraisers page
Special Events/Celebratory Events
Updates

Target Market(s)

Brides, Wedding Planners, Corporate Event Planners, Destination Companies, Public

Industry/Entity Type

Event Planning

Contact Information for Business Card

name , phone number and email address
images of party images...wedding cake- balloons-party hat etc

Logo Text

Dana Ruth Korvatch Event Design @ The Bayview Harbor Rowing Society

Number of Pages Required

4 page

Font styles to use
Decorative

Colors

Designer to choose colors to be used in the design.

Requirements
Must have
• Dana Ruth Korvatch Event Design
• @ Bayview Harbor Rowing Society
• 415-555-0193
• drkeventstudio@example-mail.net
• back side of card - Image of Bayview Harbor Rowing Society
Nice to have
• fun and catchy party images
• wedding cake - diamond ring -balloons - party hat- flowers
• would like to see the images in white, gold and silver
Should not have
• photographic pictures

```html
<!DOCTYPE html>
<html lang="en">
<head>
<meta charset="utf-8">
<title>Dana Ruth Korvatch Event Design</title>
<link rel="stylesheet" href="https://fonts.googleapis.com/css2?family=Libre+Baskerville:wght@400&family=Lato:wght@300;400;700&display=swap">
<style>
:root{
  --ink:#2b2b2b;
  --muted:#6d6d6d;
  --band:#4b4b4b;
  --white:#ffffff;
  --line:#9a9a9a;
  --black:#000000;
  --star:#f2c230;
  --serif:"Libre Baskerville", "Times New Roman", serif;
  --sans:"Lato", Arial, sans-serif;
}
*{box-sizing:border-box;margin:0;padding:0}
html,body{width:1200px;height:4196px;overflow:hidden;background:var(--white);color:var(--ink);font-family:var(--sans)}
.page{position:relative;width:1200px;height:4196px;overflow:hidden}
.abs{position:absolute}
.center{left:0;width:1200px;text-align:center}
.btn{display:inline-block;border:2px solid var(--line);border-radius:30px;font-family:var(--serif);font-size:14px;letter-spacing:.5px;text-transform:uppercase;height:46px;line-height:42px;width:172px;text-align:center;color:var(--ink);background:transparent}
.section-title{font-family:var(--serif);font-weight:400;font-size:26px;letter-spacing:1.5px;text-transform:uppercase;color:var(--ink)}

/* brand name, set as plain text */
.brand-name{font-family:var(--serif);font-size:19px;letter-spacing:1px;color:var(--white);white-space:nowrap}

/* hero */
.hero{top:0;left:0;width:1200px;height:720px}
.hero-photo{position:absolute;inset:0;background:
  linear-gradient(180deg,rgba(60,45,40,.15) 0%,rgba(60,45,40,0) 30%,rgba(90,70,60,.35) 70%,rgba(60,45,40,.6) 100%),
  linear-gradient(90deg,#c9a79b 0%,#e3c4bd 12%,#b39a86 24%,#8c7766 36%,#a28f80 48%,#9aa0a8 60%,#b3b8c0 72%,#8f8a86 84%,#c7bcb2 94%,#a7978a 100%)}
.hero-shade{position:absolute;inset:0;background:rgba(40,30,30,.22)}
.hero-curve{position:absolute;left:0;top:0}
.brand{position:absolute;left:40px;top:44px}
.menu{position:absolute;right:42px;top:48px;width:34px}
.menu span{display:block;height:4px;background:var(--white);border-radius:2px;margin-bottom:7px}
.hero-kicker{top:238px;font-family:var(--serif);font-size:38px;color:var(--white);letter-spacing:1px}
.hero-title{top:282px;font-family:var(--serif);font-weight:400;font-size:70px;color:var(--white);letter-spacing:1px}
.hero-sub{top:376px;font-size:14px;color:var(--white)}
.hero-actions{top:418px}
.hero-actions .btn{color:var(--white);border-color:var(--white);background:rgba(0,0,0,.15);margin:0 6px}
.hero-actions .btn.solid{background:var(--white);color:var(--ink)}
.scroll-down{position:absolute;left:575px;top:690px;width:50px;height:50px;border-radius:50%;background:var(--white);border:2px solid #555}

/* about */
.about-bg{top:860px;left:0;width:1200px;height:400px;background:
  linear-gradient(180deg,rgba(255,255,255,1) 0%,rgba(255,255,255,.35) 45%,rgba(255,255,255,0) 100%),
  linear-gradient(90deg,#e6d8e4 0%,#f3eef2 20%,#dccfe0 40%,#f0e8ee 60%,#d9cde0 80%,#ece4ec 100%)}
.about-title{top:790px}
.about-copy{top:846px;left:250px;width:700px;text-align:center;font-size:13px;line-height:1.55;color:var(--muted)}
.about-copy p+p{margin-top:12px}
.about-action{top:982px}

/* services */
.services{top:1253px;left:0;width:1200px;height:403px;background:var(--band)}
.service{position:absolute;width:360px;text-align:center;color:var(--white)}
.service-photo{position:absolute;width:296px;height:296px;border-radius:50%;border:6px solid #555;box-shadow:0 4px 14px rgba(0,0,0,.35)}
.service h3{position:absolute;left:0;width:360px;top:1449px;font-family:var(--serif);font-weight:400;font-size:17px;text-transform:uppercase;letter-spacing:.3px}
.service p{position:absolute;left:45px;width:270px;top:1480px;font-size:13px;line-height:1.3}
.plus{position:absolute;top:1542px;width:26px;height:26px}

/* gallery */
.gallery-title{top:1714px}
.tile{position:absolute}
.tile.raised{box-shadow:0 8px 24px rgba(0,0,0,.45);z-index:2}
.gallery-action{top:2831px}

/* testimonials */
.testimonials{top:2956px;left:0;width:1200px;height:400px;background:var(--band);color:var(--white)}
.testimonials .section-title{color:var(--white);font-size:24px}
.quote-mark{position:absolute;font-family:var(--serif);font-size:80px;line-height:1;color:var(--white)}
.quote-text{position:absolute;left:310px;width:580px;top:144px;text-align:center;font-size:14px;line-height:1.5}
.client{position:absolute;left:0;width:1200px;top:210px;text-align:center;font-family:var(--serif);font-size:18px;letter-spacing:1px}
.stars{position:absolute;left:0;width:1200px;top:244px;text-align:center;color:var(--star);font-size:16px;letter-spacing:1px}
.testimonials .btn{position:absolute;left:514px;top:278px;color:var(--white);border-color:#bdbdbd}
.dots{position:absolute;right:40px;top:178px;width:6px}
.dots span{display:block;width:5px;height:5px;border-radius:50%;background:var(--white);margin-bottom:7px}

/* contact */
.contact-bg{top:3356px;left:0;width:1200px;height:540px;background:
  linear-gradient(180deg,rgba(255,255,255,.55),rgba(255,255,255,.2)),
  linear-gradient(90deg,#fbf3ea 0%,#f9dcc0 30%,#fbe9da 50%,#f7d8c4 68%,#e8f1f6 85%,#cfe6f2 100%)}
.contact-title{top:3434px;color:#8a8a8a}
.field{position:absolute;border:2px solid #c9c9c9;border-radius:22px;font-family:var(--serif);font-style:italic;font-size:13px;color:#9a9a9a;padding:14px 18px;background:rgba(255,255,255,.35)}
.send{position:absolute;left:319px;top:3664px;width:563px;height:50px;line-height:46px;border:2px solid #c9c9c9;border-radius:25px;text-align:center;font-family:var(--serif);font-size:14px;color:#9a9a9a;letter-spacing:.5px}

/* footer */
.footer-curve{left:0;top:3760px}
.footer{left:0;top:3860px;width:1200px;height:336px;background:var(--black);color:var(--white)}
.footer-brand{position:absolute;left:40px;top:58px}
.footer-brand .brand-name{font-size:17px}
.footer-about{position:absolute;left:40px;top:102px;width:240px;font-size:12px;line-height:1.4}
.footer-more{position:absolute;left:40px;top:166px;font-family:var(--serif);font-style:italic;font-size:12px;text-decoration:underline}
.fcol{position:absolute;top:54px}
.fcol h4{font-family:var(--serif);font-weight:400;font-size:17px;letter-spacing:.5px;text-transform:uppercase;margin-bottom:20px}
.fcol li{list-style:none;font-size:12px;line-height:22px}
.fcol li::before{content:"›";margin-right:8px}
.fcontact li{display:flex;align-items:flex-start;gap:8px;line-height:17px}
.fcontact li::before{content:none}
.fcontact svg{flex:none;margin-top:2px}
.newsletter-box{position:absolute;left:1012px;top:102px;width:150px;height:78px;border:1px solid var(--white)}
.newsletter-box .label{font-family:var(--serif);font-style:italic;font-size:11px;padding:8px}
.subscribe{position:absolute;left:1012px;top:146px;width:150px;height:34px;background:var(--white);color:var(--black);font-family:var(--serif);font-size:12px;text-align:center;line-height:34px;text-transform:uppercase}
.footer-rule{position:absolute;left:40px;right:40px;top:258px;height:1px;background:#444}
.copyright{position:absolute;left:40px;top:276px;font-size:12px}
.legal{position:absolute;right:40px;top:276px;font-size:12px}
</style>
</head>
<body>
<div class="page">

  <header class="abs hero">
    <div class="hero-photo" role="img" aria-label="Elegant banquet table with pink flowers, glassware and candles in a softly lit venue"></div>
    <div class="hero-shade"></div>
    <svg class="hero-curve" width="1200" height="720" viewBox="0 0 1200 720" aria-hidden="true">
      <path d="M0,560 Q600,775 1200,560 L1200,720 L0,720 Z" fill="#ffffff"/>
    </svg>
    <div class="brand"><div class="brand-name">Dana Ruth Korvatch</div></div>
    <div class="menu" aria-label="Menu"><span></span><span></span><span></span></div>
    <div class="abs center hero-kicker">PROFESSIONAL</div>
    <h1 class="abs center hero-title">EVENT PLANNING</h1>
    <div class="abs center hero-sub">Lorem Ipsum is simply dummy text of the printing and typesetting industry.</div>
    <div class="abs center hero-actions">
      <span class="btn">Read More</span><span class="btn solid">Online Request</span>
    </div>
    <div class="scroll-down">
      <svg width="46" height="46" viewBox="0 0 46 46"><path d="M15,19 L23,27 L31,19" fill="none" stroke="#444" stroke-width="2.5"/></svg>
    </div>
  </header>

  <div class="abs about-bg" role="img" aria-label="Soft field of pale pink and white flowers"></div>
  <h2 class="abs center section-title about-title">About Us</h2>
  <div class="abs about-copy">
    <p>Lorem Ipsum is simply dummy text of the printing and typesetting industry. Lorem Ipsum has been the industry's standard dummy text ever since the 1500s, when an unknown printer took a galley of type and scrambled it to make a type specimen book.</p>
    <p>It has survived not only five centuries, but also the leap into electronic typesetting, remaining essentially unchanged.</p>
  </div>
  <div class="abs center about-action"><span class="btn">Read More</span></div>

  <div class="abs services"></div>
  <div class="abs service" style="left:63px;top:0">
    <div class="service-photo" role="img" aria-label="Wedding reception with warm string lights and long dining tables" style="left:32px;top:1102px;background:linear-gradient(180deg,#2a160c 0%,#6b3a1a 22%,#e8a050 40%,#b8682c 55%,#f2c08a 70%,#7a4622 85%,#3a2010 100%)"></div>
    <h3>Wedding Events</h3>
    <p>Lorem Ipsum is simply dummy text of the printing and typesetting industry.</p>
  </div>
  <div class="abs service" style="left:420px;top:0">
    <div class="service-photo" role="img" aria-label="Corporate conference hall with a stage screen and round tables" style="left:32px;top:1102px;background:linear-gradient(180deg,#9aa4c0 0%,#d8e2f4 25%,#6a78a8 42%,#f0f0f4 60%,#3e4460 78%,#23263a 100%)"></div>
    <h3>Corporate Meetings</h3>
    <p>Lorem Ipsum is simply dummy text of the printing and typesetting industry.</p>
  </div>
  <div class="abs service" style="left:777px;top:0">
    <div class="service-photo" role="img" aria-label="Outdoor celebration table under pink balloons on a green lawn" style="left:32px;top:1102px;background:linear-gradient(180deg,#6e9a4a 0%,#d7a0cc 20%,#8cb860 36%,#f4f2f0 55%,#c9c4cc 66%,#5c8a3a 82%,#3a5a26 100%)"></div>
    <h3>Special/Celebratory Events</h3>
    <p>Lorem Ipsum is simply dummy text of the printing and typesetting industry.</p>
  </div>
  <svg class="plus" style="left:230px" viewBox="0 0 26 26"><circle cx="13" cy="13" r="12" fill="#fff"/><path d="M13,7V19M7,13H19" stroke="#4b4b4b" stroke-width="2.5"/></svg>
  <svg class="plus" style="left:587px" viewBox="0 0 26 26"><circle cx="13" cy="13" r="12" fill="#fff"/><path d="M13,7V19M7,13H19" stroke="#4b4b4b" stroke-width="2.5"/></svg>
  <svg class="plus" style="left:944px" viewBox="0 0 26 26"><circle cx="13" cy="13" r="12" fill="#fff"/><path d="M13,7V19M7,13H19" stroke="#4b4b4b" stroke-width="2.5"/></svg>

  <h2 class="abs center section-title gallery-title">Gallery</h2>
  <div class="tile" role="img" aria-label="Banquet tent with purple lighting and white-draped round tables" style="left:42px;top:1798px;width:546px;height:320px;background:linear-gradient(180deg,#a67cc8 0%,#d6c2ec 25%,#f2eef6 45%,#8e76b4 62%,#ece6f2 78%,#6a5a8a 100%)"></div>
  <div class="tile raised" role="img" aria-label="Dimly lit dining room with set tables" style="left:588px;top:1796px;width:572px;height:322px;background:linear-gradient(180deg,#3a3632 0%,#1c1a18 35%,#2e2a26 60%,#151311 100%)">
    <svg style="position:absolute;left:262px;top:136px" width="50" height="50" viewBox="0 0 50 50"><circle cx="20" cy="20" r="14" fill="none" stroke="#fff" stroke-width="3"/><path d="M20,13V27M13,20H27" stroke="#fff" stroke-width="3"/><path d="M30,30L44,44" stroke="#fff" stroke-width="5" stroke-linecap="round"/></svg>
  </div>
  <div class="tile" role="img" aria-label="Close view of wine glasses on a banquet table with gold chairs" style="left:42px;top:2118px;width:560px;height:318px;background:linear-gradient(180deg,#c9a468 0%,#ead6ae 25%,#b89058 40%,#f4eee2 62%,#e2d4bc 80%,#c8a870 100%)"></div>
  <div class="tile" role="img" aria-label="Candlelit tables under magenta lighting" style="left:602px;top:2118px;width:556px;height:318px;background:linear-gradient(180deg,#2a0e3a 0%,#6a1e8a 30%,#c0308a 50%,#e86a50 62%,#8a2a90 78%,#2a0e3a 100%)"></div>
  <div class="tile" role="img" aria-label="Round table with navy chair covers and blue centrepiece" style="left:42px;top:2436px;width:560px;height:320px;background:linear-gradient(180deg,#6a4a2a 0%,#2a1e14 25%,#2c2c5a 45%,#5a5a9a 55%,#2a1e14 75%,#14100a 100%)"></div>
  <div class="tile" role="img" aria-label="Bright white marquee with pink floral table settings" style="left:602px;top:2436px;width:556px;height:320px;background:linear-gradient(180deg,#e6e0da 0%,#f8f6f4 30%,#ffffff 50%,#f0c8d0 68%,#fafafa 82%,#e8d8da 100%)"></div>
  <div class="abs center gallery-action"><span class="btn">View More</span></div>

  <section class="abs testimonials">
    <h2 class="abs center section-title" style="top:90px">What Our Clients Say`s</h2>
    <div class="quote-mark" style="left:274px;top:128px">“</div>
    <div class="quote-mark" style="left:892px;top:128px">”</div>
    <p class="quote-text">Lorem Ipsum is simply dummy text of the printing and typesetting industry. Lorem Ipsum has been the industry's standard dummy text ever since the 1500s</p>
    <div class="client">MARCUS ELLERY</div>
    <div class="stars">★★★★★</div>
    <span class="btn">View More</span>
    <div class="dots"><span></span><span></span><span></span></div>
  </section>

  <div class="abs contact-bg" role="img" aria-label="Faint pastel party balloons on a pale background"></div>
  <h2 class="abs center section-title contact-title">Contact Us</h2>
  <div class="field" style="left:319px;top:3500px;width:277px;height:48px">Full Name</div>
  <div class="field" style="left:604px;top:3500px;width:278px;height:48px">Email Address</div>
  <div class="field" style="left:319px;top:3554px;width:563px;height:104px">Your Message</div>
  <div class="send">SEND NOW</div>

  <svg class="abs footer-curve" width="1200" height="101" viewBox="0 0 1200 101" aria-hidden="true">
    <path d="M0,101 L0,60 Q600,-40 1200,60 L1200,101 Z" fill="#000"/>
  </svg>
  <footer class="abs footer">
    <div class="footer-brand"><div class="brand-name">Dana Ruth Korvatch</div></div>
    <p class="footer-about">Lorem Ipsum is simply dummy text of the printing and typesetting industry.</p>
    <span class="footer-more">READ MORE</span>

    <div class="fcol" style="left:313px">
      <h4>Quick Links</h4>
      <ul><li>Home</li><li>About us</li><li>Services</li><li>Gallery</li><li>Blog</li><li>Contact us</li></ul>
    </div>
    <div class="fcol" style="left:534px">
      <h4>Useful Links</h4>
      <ul><li>Login</li><li>Register</li><li>Book Your Event</li></ul>
    </div>
    <div class="fcol fcontact" style="left:764px">
      <h4>Contact Us</h4>
      <ul>
        <li><svg width="11" height="11" viewBox="0 0 12 12"><path d="M2,1 L4.5,1 L5.5,4 L4,5 Q5,7.5 7,8 L8,6.5 L11,7.5 L11,10 Q11,11 10,11 Q1,10 1,2 Q1,1 2,1Z" fill="#fff"/></svg>415-555-0193</li>
        <li><svg width="11" height="11" viewBox="0 0 12 12"><path d="M2,1 L4.5,1 L5.5,4 L4,5 Q5,7.5 7,8 L8,6.5 L11,7.5 L11,10 Q11,11 10,11 Q1,10 1,2 Q1,1 2,1Z" fill="#fff"/></svg>415-555-0148</li>
        <li><svg width="12" height="10" viewBox="0 0 12 10"><rect x=".5" y=".5" width="11" height="9" fill="none" stroke="#fff"/><path d="M.5,.5 L6,5.5 L11.5,.5" fill="none" stroke="#fff"/></svg>drkeventstudio@example-mail.net</li>
        <li><svg width="10" height="13" viewBox="0 0 10 13"><path d="M5,12 Q0,6 0,5 A5,5 0 0 1 10,5 Q10,6 5,12Z" fill="#fff"/><circle cx="5" cy="5" r="2" fill="#000"/></svg>42 Harbor Point Road<br>Bayview, CA 94124</li>
      </ul>
    </div>
    <div class="fcol" style="left:1012px"><h4>Newsletter</h4></div>
    <div class="newsletter-box"><div class="label">Email Address</div></div>
    <div class="subscribe">Subscribe</div>

    <div class="footer-rule"></div>
    <div class="copyright">© Copyright 2019 Dana Ruth Korvatch - All Right Reserved</div>
    <div class="legal">Privacy Policy · Terms &amp; Conditions</div>
  </footer>

</div>
</body>
</html>
```